International Sustainable Cities NGO needs PPT Design

We need a PPT design for a presentation upcoming at a leading university on the East coast. The design needs to be clean and simple, professional and room for photos and maps. It's a presentation about citizen mapping and data collection for city planning/decision making.

Industry/Entity Type

University

```html
<!DOCTYPE html>
<html lang="en">
<head>
<meta charset="utf-8">
<title>Metroscope – Presentation Slide Set</title>
<link rel="stylesheet" href="https://fonts.googleapis.com/css2?family=Antonio:wght@100;200&family=Roboto:ital,wght@0,300;0,400;0,500;0,700;1,900&family=Lora&display=swap">
<style>
:root{
  --canvas:#dcdcdc;
  --paper:#ffffff;
  --ink:#333333;
  --title-ink:#444444;
  --muted:#777777;
  --teal:#4cc29b;
  --teal-panel:#4e9e8f;
  --navy:#24457a;
  --night:#2d4a78;
  --night-deep:#1f3560;
  --grey-panel:#7d7672;
  --pink:#d6186c;
  --violet:#4c3f8f;
  --bar-dark:#3a3a3a;
}
*{box-sizing:border-box;margin:0;padding:0}
html,body{width:1200px;height:1200px;overflow:hidden;background:var(--canvas)}
body{font-family:"Roboto",sans-serif;color:var(--ink)}
.board{display:grid;grid-template-columns:repeat(3,378px);grid-auto-rows:214px;column-gap:16px;row-gap:22px;padding:22px}
.slide{position:relative;overflow:hidden;background:var(--paper)}
.slide > *{position:absolute}
.title{font-family:"Antonio",sans-serif;font-weight:100;font-size:28px;line-height:1;text-transform:uppercase;color:var(--title-ink);letter-spacing:0}
.title.right{text-align:right}
.title.light{color:#fff}
.brand{font-family:"Roboto",sans-serif;font-weight:500;font-size:16px;color:var(--navy);letter-spacing:-.3px;white-space:nowrap}
.mark{right:12px;bottom:8px;font-family:"Roboto",sans-serif;font-weight:500;font-size:5px;letter-spacing:1.2px;line-height:1.25;color:#3c6b7a;text-align:center}
.tiny{font-size:4.2px;line-height:1.35;color:var(--muted)}
.url{font-size:4.2px;color:var(--muted)}
.name{font-weight:900;font-style:italic;font-size:10px;color:var(--ink);text-transform:uppercase}
.caption{font-weight:900;font-style:italic;font-size:5.5px;color:var(--ink)}
.year{font-size:4.5px;color:var(--muted)}
.photo-leaf{background:linear-gradient(135deg,#d9d2a8 0%,#a6ad78 40%,#56703e 75%,#2f4a24 100%)}
.photo-bloom{background:linear-gradient(160deg,#5a5f8a 0%,#8a7fa6 40%,#6b7a4b 75%,#3e4a2c 100%)}
.photo-road{background:linear-gradient(180deg,#6b6d2c 0%,#9a9a45 30%,#5e4d33 55%,#2e2a24 100%)}
.photo-sky{background:linear-gradient(180deg,#6aa3cf 0%,#b9d4e6 45%,#8fb36a 70%,#9a9a8a 100%)}
.illus{background:linear-gradient(120deg,#2d4a78 0%,#34588a 45%,#4f8a5a 80%,#5e9a4c 100%)}
.skill{height:1.6px;background:#ddd}
.skill i{display:block;height:100%;background:var(--teal)}
.skill.dark i{background:var(--bar-dark)}
.avatar{border-radius:50%;background:linear-gradient(135deg,#d9c3ad,#a88a6e)}
</style>
</head>
<body>
<main class="board">

  <!-- 1 cover -->
  <section class="slide">
    <div class="illus" role="img" aria-label="Felt-craft illustration of a green city globe with wind turbines, trees, buildings and a sun" style="left:0;top:0;width:378px;height:214px"></div>
    <div style="left:14px;top:48px;width:134px;height:118px;background:#fff;text-align:center;padding-top:20px">
      <div class="brand" style="position:static;font-size:18px">Metroscope</div>
      <div style="font-weight:500;font-size:8.5px;letter-spacing:2px;line-height:1.25;color:#3c6b7a;margin-top:12px">GREENPATH<br>BUILDERS</div>
      <div style="font-family:'Lora',serif;font-size:7.5px;color:var(--muted);margin-top:12px">Tomasz Nowak</div>
    </div>
  </section>

  <!-- 2 agenda -->
  <section class="slide" style="background:linear-gradient(180deg,var(--night),var(--night-deep))">
    <div role="img" aria-label="Felt-craft illustration of a round planet covered with city buildings, parks and roads" style="left:0;top:0;width:220px;height:214px;background:linear-gradient(90deg,#34588a 0%,#4f8a5a 45%,#3f78ad 70%,rgba(45,74,120,0) 100%)"></div>
    <div style="left:226px;top:34px;color:#fff">
      <div class="name" style="color:#fff;font-size:12px">01.</div>
      <div class="tiny" style="color:#c9d3e6">Neighbourhood map walks<br>Open data workshops</div>
      <div class="name" style="color:#fff;font-size:12px;margin-top:10px">02.</div>
      <div class="tiny" style="color:#c9d3e6">Resident surveys<br>Street condition reports</div>
      <div class="name" style="color:#fff;font-size:12px;margin-top:10px">03.</div>
      <div class="tiny" style="color:#c9d3e6">Transit feedback<br>Park access audits<br>Results for city councils</div>
      <div class="name" style="color:#fff;font-size:12px;margin-top:10px">04.</div>
      <div class="tiny" style="color:#c9d3e6">Next steps</div>
    </div>
  </section>

  <!-- 3 team -->
  <section class="slide">
    <div class="title" style="left:34px;top:30px">Our<br>Awesome<br>Team</div>
    <p class="tiny" style="left:34px;top:122px;width:56px">Our team brings planners, students and residents together to map the city block by block.</p>
    <svg role="img" aria-label="Blurred leaf photograph cut into diagonal strips" style="left:120px;top:0" width="258" height="214" viewBox="0 0 258 214">
      <defs><linearGradient id="leafStrip" x1="0" y1="1" x2="1" y2="0"><stop offset="0" stop-color="#e8dfb8"/><stop offset=".45" stop-color="#a9ad78"/><stop offset="1" stop-color="#3f5f2e"/></linearGradient></defs>
      <g fill="url(#leafStrip)">
        <polygon points="10,178 180,88 184,96 14,186"/>
        <polygon points="40,192 236,80 240,94 44,206"/>
        <polygon points="70,206 250,104 254,114 74,214"/>
        <polygon points="60,150 230,54 234,66 64,162"/>
        <polygon points="90,120 250,30 254,42 94,132"/>
        <polygon points="110,86 246,10 250,20 114,96"/>
        <polygon points="170,40 240,2 244,10 174,48"/>
      </g>
    </svg>
    <div class="mark">GREENPATH<br>BUILDERS</div>
  </section>

  <!-- 4 single team -->
  <section class="slide">
    <div style="left:0;top:0;width:113px;height:214px;background:var(--grey-panel)"></div>
    <div class="title right light" style="left:0;top:24px;width:96px">Single<br>Team<br>Slide</div>
    <div style="left:86px;top:114px;width:0;height:0;border-left:10px solid transparent;border-top:10px solid #fff"></div>
    <div class="url" style="left:42px;top:182px;color:#d8d3cf">www.yourwebsitehere.com</div>
    <div class="photo-leaf" role="img" aria-label="Soft-focus photograph of hanging leaves against a pale background" style="left:113px;top:0;width:265px;height:214px"></div>
    <p class="tiny" style="left:276px;top:68px;width:58px;color:rgba(255,255,255,.65)">Local volunteers lead our mapping days in every ward.</p>
    <div class="skill" style="left:276px;top:164px;width:62px;background:rgba(255,255,255,.3)"><i style="width:78%"></i></div>
    <div class="skill dark" style="left:276px;top:172px;width:62px;background:rgba(255,255,255,.3)"><i style="width:68%;background:#fff"></i></div>
  </section>

  <!-- 5 two picture -->
  <section class="slide">
    <div class="title right" style="left:20px;top:22px;width:108px">Two<br>Picture<br>Slide</div>
    <div class="brand" style="left:40px;top:112px">Metroscope</div>
    <p class="tiny" style="left:28px;top:134px;width:102px;text-align:right">Residents collect street data with phones, and planners turn it into clear city maps.</p>
    <div class="url" style="left:74px;top:184px">www.yourwebsitehere.com</div>
    <div class="photo-bloom" role="img" aria-label="Photograph of dandelion seed heads in a meadow" style="left:180px;top:28px;width:72px;height:126px"></div>
    <div class="photo-leaf" role="img" aria-label="Soft-focus photograph of hanging leaves" style="left:267px;top:28px;width:73px;height:126px"></div>
    <div class="caption" style="left:180px;top:160px;width:72px;text-align:center">YOUR TITLE</div>
    <p class="tiny" style="left:180px;top:169px;width:72px;text-align:center">Short note about this photo.</p>
    <div class="caption" style="left:267px;top:160px;width:73px;text-align:center">YOUR TITLE</div>
    <p class="tiny" style="left:267px;top:169px;width:73px;text-align:center">Short note about this photo.</p>
    <div class="mark">GREENPATH<br>BUILDERS</div>
  </section>

  <!-- 6 two picture variant -->
  <section class="slide">
    <div class="title right" style="left:20px;top:22px;width:108px">Two<br>Picture<br>Slide</div>
    <div class="brand" style="left:32px;top:112px">Metroscope</div>
    <div class="url" style="left:74px;top:182px">www.yourwebsitehere.com</div>
    <p class="tiny" style="left:168px;top:28px;width:156px">Shared maps show where people walk, wait and gather, giving planners a clearer view of daily life in the city.<br><br>— The Quotes</p>
    <div class="photo-bloom" role="img" aria-label="Photograph of dandelion seed heads" style="left:164px;top:86px;width:74px;height:42px"></div>
    <div class="photo-leaf" role="img" aria-label="Soft-focus photograph of leaves" style="left:260px;top:86px;width:74px;height:42px"></div>
    <div class="caption" style="left:168px;top:136px">Your Title</div>
    <div class="tiny" style="left:168px;top:143px">Founder</div>
    <div class="caption" style="left:266px;top:136px">Your Title</div>
    <div class="tiny" style="left:266px;top:143px">Founder</div>
    <div class="tiny" style="left:168px;top:155px">Mapping</div><div class="skill" style="left:168px;top:162px;width:56px"><i style="width:80%"></i></div>
    <div class="tiny" style="left:168px;top:166px">Survey</div><div class="skill dark" style="left:168px;top:173px;width:56px"><i style="width:70%"></i></div>
    <div class="tiny" style="left:266px;top:155px">Mapping</div><div class="skill" style="left:266px;top:162px;width:56px"><i style="width:80%"></i></div>
    <div class="tiny" style="left:266px;top:166px">Survey</div><div class="skill dark" style="left:266px;top:173px;width:56px"><i style="width:70%"></i></div>
    <div class="mark">GREENPATH<br>BUILDERS</div>
  </section>

  <!-- 7 best designer -->
  <section class="slide">
    <div class="photo-leaf" role="img" aria-label="Soft-focus photograph of leaves as a header band" style="left:0;top:0;width:378px;height:93px"></div>
    <div style="left:118px;top:33px;width:0;height:0;border-left:8px solid transparent;border-bottom:8px solid var(--teal)"></div>
    <div class="name" style="left:56px;top:48px;color:#fff">YOUR NAME</div>
    <div style="left:30px;top:62px;width:100px;height:.6px;background:rgba(255,255,255,.7)"></div>
    <div class="tiny" style="left:98px;top:66px;color:#fff">Art Director</div>
    <div class="title" style="left:42px;top:112px">Best<br>Designer</div>
    <div class="url" style="left:74px;top:184px">www.yourwebsitehere.com</div>
    <div class="caption" style="left:178px;top:114px">Your Title</div>
    <p class="tiny" style="left:184px;top:122px;width:100px">Leads field mapping across partner neighbourhoods and shares results</p>
    <div class="tiny" style="left:178px;top:146px">Mapping</div><div class="skill" style="left:178px;top:153px;width:104px"><i style="width:80%"></i></div>
    <div class="tiny" style="left:178px;top:157px">Survey</div><div class="skill dark" style="left:178px;top:164px;width:104px"><i style="width:70%"></i></div>
    <div class="brand" style="right:26px;top:118px;font-size:12px">Metroscope</div>
    <div style="right:12px;top:104px;width:0;height:0;border-left:16px solid transparent;border-top:16px solid var(--teal)"></div>
    <div class="mark">GREENPATH<br>BUILDERS</div>
  </section>

  <!-- 8 timeline picture -->
  <section class="slide">
    <div class="title right" style="left:12px;top:22px;width:108px">Timeline<br>Picture<br>Slide</div>
    <div class="brand" style="left:20px;top:112px">Metroscope</div>
    <div class="url" style="left:44px;top:186px">www.yourwebsitehere.com</div>
    <div style="left:158px;top:0;width:.8px;height:214px;background:#c9d6df"></div>
    <div class="year" style="left:138px;top:91px">2015</div>
    <div style="left:155px;top:90px;width:7px;height:7px;border:.8px solid #9fb6c4;border-radius:50%;background:#fff"></div>
    <div class="avatar" role="img" aria-label="Portrait photo of a team member" style="left:138px;top:34px;width:44px;height:44px"></div>
    <div class="name" style="left:190px;top:48px">YOUR NAME</div>
    <div class="tiny" style="left:190px;top:60px">Designer</div>
    <div class="caption" style="left:178px;top:89px">Your Title Goes Here</div>
    <p class="tiny" style="left:178px;top:97px;width:140px">Volunteers mapped forty blocks of the east district this year.</p>
    <div class="photo-bloom" role="img" aria-label="Wide photograph of dandelions in a meadow" style="left:178px;top:122px;width:166px;height:68px"></div>
    <div class="mark">GREENPATH<br>BUILDERS</div>
  </section>

  <!-- 9 timeline continued -->
  <section class="slide">
    <div style="left:153px;top:0;width:.8px;height:214px;background:#c9d6df"></div>
    <div class="year" style="left:135px;top:26px">2015</div>
    <div class="caption" style="left:170px;top:24px">Your Title Goes Here</div>
    <p class="tiny" style="left:170px;top:33px;width:108px">First citizen map of bus stops and benches, shared with the planning office.</p>
    <div class="photo-bloom" role="img" aria-label="Photograph of dandelions" style="left:170px;top:65px;width:48px;height:62px"></div>
    <div class="photo-road" role="img" aria-label="Photograph of an open road under a cloudy sky" style="left:221px;top:65px;width:50px;height:30px"></div>
    <div class="photo-road" role="img" aria-label="Photograph of a country road at dusk" style="left:221px;top:97px;width:50px;height:30px"></div>
    <div class="photo-leaf" role="img" aria-label="Soft-focus photograph of leaves" style="left:274px;top:65px;width:78px;height:62px"></div>
    <div class="year" style="left:135px;top:152px">2015</div>
    <div class="caption" style="left:170px;top:150px">Your Title Goes Here</div>
    <p class="tiny" style="left:170px;top:159px;width:150px">Second round of surveys added parks, crossings and lighting data for the city council review.<br>— The Quotes</p>
    <div class="mark">GREENPATH<br>BUILDERS</div>
  </section>

  <!-- 10 timeline skills -->
  <section class="slide">
    <div style="left:158px;top:0;width:.8px;height:214px;background:#c9d6df"></div>
    <div class="year" style="left:138px;top:26px">2015</div>
    <div style="left:155px;top:26px;width:7px;height:7px;border:.8px solid #9fb6c4;border-radius:50%;background:#fff"></div>
    <div class="caption" style="left:176px;top:25px">Your Title Goes Here</div>
    <div class="tiny" style="left:176px;top:37px">Mapping</div><div class="skill" style="left:176px;top:43px;width:120px"><i style="width:85%"></i></div>
    <div class="tiny" style="left:176px;top:47px">Surveys</div><div class="skill" style="left:176px;top:53px;width:120px"><i style="width:78%;background:var(--pink)"></i></div>
    <div class="tiny" style="left:176px;top:57px">Photography</div><div class="skill" style="left:176px;top:63px;width:120px"><i style="width:70%;background:var(--violet)"></i></div>
    <div class="tiny" style="left:176px;top:67px">Web Design</div><div class="skill" style="left:176px;top:73px;width:120px"><i style="width:60%;background:#888"></i></div>
    <div style="left:176px;top:86px;width:136px;height:40px;background:#efefef"></div>
    <div style="left:190px;top:98px;width:9px;height:13px;border:.8px solid #aaa"></div>
    <p class="tiny" style="left:222px;top:96px;width:76px">Notes from the mapping team about this year's work in the field.</p>
    <div class="avatar" role="img" aria-label="Portrait photo of a team member" style="left:138px;top:145px;width:40px;height:40px"></div>
    <div class="name" style="left:189px;top:158px">YOUR NAME</div>
    <div class="tiny" style="left:189px;top:170px">Designer</div>
    <div class="mark">GREENPATH<br>BUILDERS</div>
  </section>

  <!-- 11 full picture -->
  <section class="slide">
    <div class="photo-road" role="img" aria-label="Photograph of an empty desert road stretching to the horizon under a yellow-green sky" style="left:0;top:0;width:378px;height:214px"></div>
    <div style="left:115px;top:0;width:116px;height:214px;background:rgba(20,30,20,.5)"></div>
    <div style="left:0;top:0;width:115px;height:214px;background:var(--teal-panel)"></div>
    <div class="title right light" style="left:0;top:24px;width:98px">Full<br>Picture<br>Slide</div>
    <div style="left:88px;top:114px;width:0;height:0;border-left:10px solid transparent;border-top:10px solid var(--teal)"></div>
    <div class="brand" style="left:16px;top:130px;color:#2f5f86">Metroscope</div>
    <div class="url" style="left:42px;top:184px;color:#d6ece6">www.yourwebsitehere.com</div>
    <p class="tiny" style="left:138px;top:68px;width:64px;color:rgba(255,255,255,.7)">Open roads link our partner towns to the region. Data from residents shows where repairs matter most.</p>
    <div class="skill" style="left:138px;top:160px;width:72px;background:rgba(255,255,255,.3)"><i style="width:80%"></i></div>
    <div class="skill" style="left:138px;top:168px;width:72px;background:rgba(255,255,255,.3)"><i style="width:70%;background:#fff"></i></div>
    <div style="left:138px;top:190px;display:flex;gap:4px">
      <span style="width:4px;height:4px;border:.6px solid #ccc"></span><span style="width:4px;height:4px;border:.6px solid #ccc"></span><span style="width:4px;height:4px;border:.6px solid #ccc"></span><span style="width:4px;height:4px;border:.6px solid #ccc"></span><span style="width:4px;height:4px;border:.6px solid #ccc"></span>
    </div>
  </section>

  <!-- 12 thank you -->
  <section class="slide">
    <div class="photo-sky" role="img" aria-label="Photograph of a traveller with a suitcase standing on a country road under a blue sky" style="left:0;top:36px;width:378px;height:178px"></div>
    <svg style="left:0;top:0" width="378" height="214" viewBox="0 0 378 214">
      <polyline points="128,0 186,60 244,0" fill="none" stroke="var(--teal)" stroke-width="6"/>
      <polygon points="12,52 26,52 12,66" fill="var(--teal)"/>
      <polygon points="366,52 352,52 366,66" fill="var(--teal)"/>
    </svg>
    <div style="left:0;top:116px;width:378px;text-align:center;font-family:'Antonio',sans-serif;font-weight:100;font-size:7px;letter-spacing:2.5px;color:rgba(255,255,255,.8)">YOUR SUBTITLE HERE</div>
    <div style="left:0;top:126px;width:378px;text-align:center;font-family:'Antonio',sans-serif;font-weight:100;font-size:30px;letter-spacing:1.5px;color:#fff">THANK YOU</div>
  </section>

  <!-- 13 column chart -->
  <section class="slide">
    <div class="title right" style="left:10px;top:22px;width:108px">Column<br>Chart<br>Slide</div>
    <div style="left:108px;top:110px;width:0;height:0;border-left:10px solid transparent;border-top:10px solid var(--pink)"></div>
    <div class="brand" style="left:8px;top:128px">Metroscope</div>
    <div class="url" style="left:54px;top:188px">www.yourwebsitehere.com</div>
    <svg style="left:158px;top:28px" width="120" height="176" viewBox="0 0 120 176" role="img" aria-label="Column chart of values from 2014 to 2017">
      <g stroke="#eee" stroke-width=".5">
        <line x1="12" y1="8" x2="118" y2="8"/><line x1="12" y1="24" x2="118" y2="24"/><line x1="12" y1="40" x2="118" y2="40"/><line x1="12" y1="56" x2="118" y2="56"/><line x1="12" y1="72" x2="118" y2="72"/><line x1="12" y1="88" x2="118" y2="88"/><line x1="12" y1="104" x2="118" y2="104"/><line x1="12" y1="120" x2="118" y2="120"/><line x1="12" y1="136" x2="118" y2="136"/>
      </g>
      <line x1="12" y1="4" x2="12" y2="152" stroke="#bbb" stroke-width=".6"/>
      <line x1="12" y1="152" x2="118" y2="152" stroke="#bbb" stroke-width=".6"/>
      <g font-size="3.5" fill="#777" text-anchor="end" font-family="Roboto,sans-serif">
        <text x="9" y="10">9</text><text x="9" y="26">8</text><text x="9" y="42">7</text><text x="9" y="58">6</text><text x="9" y="74">5</text><text x="9" y="90">4</text><text x="9" y="106">3</text><text x="9" y="122">2</text><text x="9" y="138">1</text><text x="9" y="154">0</text>
      </g>
      <rect x="20" y="104" width="10" height="16" fill="#555"/><rect x="20" y="120" width="10" height="32" fill="var(--teal)"/>
      <rect x="45" y="72" width="10" height="48" fill="#555"/><rect x="45" y="120" width="10" height="32" fill="var(--teal)"/>
      <rect x="70" y="64" width="10" height="40" fill="#555"/><rect x="70" y="104" width="10" height="48" fill="var(--teal)"/>
      <rect x="95" y="14" width="10" height="56" fill="#555"/><rect x="95" y="70" width="10" height="82" fill="var(--teal)"/>
      <g font-size="3.5" fill="#777" text-anchor="middle" font-family="Roboto,sans-serif">
        <text x="25" y="159">2014</text><text x="50" y="159">2015</text><text x="75" y="159">2016</text><text x="100" y="159">2017</text>
      </g>
    </svg>
    <p class="tiny" style="left:292px;top:48px;width:76px">Column charts compare values across years. Each bar shows mapped sites split by source.<br><br>Resident reports grew every year as more people joined the mapping days across the city.</p>
    <div class="mark">GREENPATH<br>BUILDERS</div>
  </section>

  <!-- 14 bar chart -->
  <section class="slide">
    <div class="title right" style="left:10px;top:22px;width:108px">Bar<br>Chart<br>Slide</div>
    <div style="left:108px;top:110px;width:0;height:0;border-left:10px solid transparent;border-top:10px solid var(--teal)"></div>
    <div class="brand" style="left:16px;top:128px">Metroscope</div>
    <div class="url" style="left:44px;top:188px">www.yourwebsitehere.com</div>
    <p class="tiny" style="left:152px;top:36px;width:190px">Bar charts show how many reports each year came from residents and partner groups, with totals growing since 2010 as more districts joined.</p>
    <svg style="left:150px;top:86px" width="220" height="106" viewBox="0 0 220 106" role="img" aria-label="Horizontal bar chart of values from 2010 to 2016">
      <g font-size="3.8" fill="#777" text-anchor="end" font-family="Roboto,sans-serif">
        <text x="20" y="8">2016</text><text x="20" y="20">2015</text><text x="20" y="32">2014</text><text x="20" y="44">2013</text><text x="20" y="56">2012</text><text x="20" y="68">2011</text><text x="20" y="80">2010</text>
      </g>
      <g stroke="#eee" stroke-width=".5"><line x1="24" y1="11" x2="210" y2="11"/><line x1="24" y1="23" x2="210" y2="23"/><line x1="24" y1="35" x2="210" y2="35"/><line x1="24" y1="47" x2="210" y2="47"/><line x1="24" y1="59" x2="210" y2="59"/><line x1="24" y1="71" x2="210" y2="71"/><line x1="24" y1="83" x2="210" y2="83"/></g>
      <rect x="24" y="5" width="68" height="3" fill="var(--bar-dark)"/><rect x="92" y="5" width="80" height="3" fill="var(--teal)"/>
      <rect x="24" y="17" width="38" height="3" fill="var(--bar-dark)"/><rect x="62" y="17" width="42" height="3" fill="var(--teal)"/>
      <rect x="24" y="29" width="15" height="3" fill="var(--bar-dark)"/><rect x="39" y="29" width="23" height="3" fill="var(--teal)"/>
      <rect x="24" y="41" width="8" height="3" fill="var(--bar-dark)"/><rect x="32" y="41" width="12" height="3" fill="var(--teal)"/>
      <rect x="24" y="53" width="6" height="3" fill="var(--bar-dark)"/><rect x="30" y="53" width="6" height="3" fill="var(--teal)"/>
      <rect x="24" y="65" width="5" height="3" fill="var(--bar-dark)"/><rect x="29" y="65" width="7" height="3" fill="var(--teal)"/>
      <rect x="24" y="77" width="4" height="3" fill="var(--bar-dark)"/><rect x="28" y="77" width="5" height="3" fill="var(--teal)"/>
      <g font-size="3.8" fill="#777" text-anchor="middle" font-family="Roboto,sans-serif">
        <text x="24" y="94">0</text><text x="54" y="94">10</text><text x="84" y="94">20</text><text x="114" y="94">30</text><text x="144" y="94">40</text><text x="174" y="94">50</text><text x="204" y="94">60</text>
      </g>
    </svg>
    <div class="mark">GREENPATH<br>BUILDERS</div>
  </section>

  <!-- 15 pie chart -->
  <section class="slide">
    <div class="title right" style="left:10px;top:22px;width:108px">Pie<br>Chart<br>Slide</div>
    <div style="left:108px;top:110px;width:0;height:0;border-left:10px solid transparent;border-top:10px solid var(--teal)"></div>
    <div class="brand" style="left:16px;top:128px">Metroscope</div>
    <div class="url" style="left:44px;top:188px">www.yourwebsitehere.com</div>
    <svg style="left:186px;top:28px" width="114" height="114" viewBox="-57 -57 114 114" role="img" aria-label="Donut chart with four segments">
      <path d="M0,-55 A55,55 0 0 1 55,0 L0,0 Z" fill="#555"/>
      <path d="M55,0 A55,55 0 0 1 0,55 L0,0 Z" fill="#8a8a8a"/>
      <path d="M0,55 A55,55 0 0 1 -47,28 L0,0 Z" fill="#cfcfcf"/>
      <path d="M-47,28 A55,55 0 0 1 0,-55 L0,0 Z" fill="var(--teal)"/>
      <circle r="30" fill="none" stroke="#fff" stroke-width="5"/>
      <circle r="24" fill="#fff"/>
    </svg>
    <div class="tiny" style="left:216px;top:148px">● 2014 &nbsp;● 2015 &nbsp;● 2016 &nbsp;● 2017</div>
    <p class="tiny" style="left:164px;top:162px;width:92px">Pie charts show shares of the whole, here the mix of reports by year.</p>
    <p class="tiny" style="left:262px;top:162px;width:92px">The largest share came from residents in the newest district.</p>
    <div class="mark">GREENPATH<br>BUILDERS</div>
  </section>

</main>
</body>
</html>
```